Modern multimedia website for Brindle Legal

Website required for a Maritime Law practice in Australia - to modernise old existing one see www.brindlelegal-example.com

Requires resizable website suitable for web, desktop, Phone and Tablet viewing.

Site has to be uncluttered, clear, elegant and modern. Has to instil, confidence, knowledge, trust. An not appear like a stuffy conservative firm.

Logo already designed (attached).

Colours - any suitable to purpose and design.

Would like to display RSS feed(s) but not essential.

Would also like to have a blog component that links to Net Wrk, Chirpa, Snapvue, Zandle + (Accounts already exist).

Already have Domain registered - Need to be able to upload files easily

All Website passwords (uploading etc) to remain with Brindle Legal.

Have attached own images (with identification and trade mark images removed for possible use.)

No images or text to be used that is protected by others copy-write or trademark to be used.

Text for web site to be provided , can be suggested or modification of current website text - am flexible

Target Market(s)

Professional organisations - Shipowners, Operators, Global companies. Luxury Yacht owners,

Industry/Entity Type

Legal

Coding

Coded - Design and coding required

Number of Pages Required

1 page

Requirements
Must have
• Be easy for me to upload to domain server - i am not a computer person.
• Site to be modern style ( flexible with page number) but must be easy and quick to load .
Nice to have
• RSS Feed with feeds from : Harrow's Ledger QMT, vBosun & Coastal -Bulletin.
Should not have
• Look like a conservative Law form.

```html
<!DOCTYPE html>
<html lang="en">
<head>
<meta charset="utf-8">
<title>Brindle Legal — Admiralty and Maritime Lawyers</title>
<link rel="stylesheet" href="https://fonts.googleapis.com/css2?family=Open+Sans:ital,wght@0,400;0,600;0,700;1,400;1,600&family=Oswald:wght@500&display=swap">
<style>
  :root{
    --blue:#0a84c8;
    --blue-dark:#0873ae;
    --ink:#333;
    --muted:#666;
    --top:#222;
    --footer:#232323;
    --footer-base:#1b1b1b;
    --soft:#f5f5f5;
    --white:#fff;
  }
  *{box-sizing:border-box;margin:0;padding:0}
  html,body{width:703px;height:1200px;overflow:hidden}
  body{position:relative;font-family:"Open Sans",Arial,sans-serif;color:var(--ink);background:var(--white)}
  .abs{position:absolute}
  a{color:inherit;text-decoration:none}

  /* top bar */
  .topbar{left:0;top:0;width:703px;height:15px;background:var(--top)}
  .topbar .socials{left:92px;top:2px;display:flex;gap:3px}
  .topbar .socials span{width:11px;height:11px;border-radius:2px;background:var(--blue);display:block}
  .topbar .mail{right:94px;top:3px;font-size:6px;color:#ccc;display:flex;align-items:center;gap:12px}

  /* header */
  .header{left:0;top:15px;width:703px;height:79px;background:var(--white)}
  .logo{left:96px;top:10px;width:60px;text-align:center}
  .logo .mark{width:22px;height:22px;border-radius:50%;border:2px solid var(--blue);margin:0 auto 2px}
  .logo .name{font-size:9px;color:var(--blue);line-height:1}
  .logo .tag{font-size:4px;color:#555;line-height:1.2}
  .share{left:300px;top:25px;font-size:8px;font-style:italic;color:#555;display:flex;align-items:center;gap:4px}
  .phone{left:435px;top:21px}
  .phone .num{font-size:8px;font-style:italic;color:#444;padding-left:17px}
  .phone .sub{font-size:4px;color:#777;padding-left:1px}
  .btn-consult{left:516px;top:14px;width:93px;height:19px;background:var(--blue);color:var(--white);font-size:6px;font-weight:700;display:flex;align-items:center;justify-content:center}
  .nav{left:298px;top:58px;display:flex;align-items:center;font-size:7px;color:#444}
  .nav .sep{color:var(--blue);margin:0 12px}
  .search{left:543px;top:58px;font-size:7px;color:#444;display:flex;align-items:center;gap:8px}

  /* hero */
  .hero{left:0;top:94px;width:703px;height:258px;background:linear-gradient(180deg,#5b86c6 0%,#8fb0dc 35%,#c9d2dd 55%,#2b3444 80%,#7a7f86 100%)}
  .hero h1{left:0;top:40px;width:703px;text-align:center;font-family:"Oswald",Impact,sans-serif;font-weight:500;font-size:27px;color:var(--white);letter-spacing:-.3px}
  .hero .lead{left:0;top:75px;width:703px;text-align:center;font-size:8px;color:var(--white)}
  .slide-arrow{top:87px;width:25px;height:28px;background:rgba(70,70,70,.75);display:flex;align-items:center;justify-content:center}
  .btn{width:76px;height:24px;background:var(--blue);color:var(--white);font-size:8px;display:flex;align-items:center;justify-content:center}

  /* intro */
  .intro{left:0;top:352px;width:703px;height:90px;text-align:center}
  .sec-title{font-size:12px;color:#222;font-weight:400}
  .sec-title b{color:var(--blue);font-weight:400}
  .intro .sec-title{margin-top:16px}
  .intro .strong{margin-top:17px;font-size:9px;color:#444;font-weight:600}
  .intro .small{margin-top:2px;font-size:6.2px;color:var(--muted)}

  /* services */
  .services{left:0;top:442px;width:703px;height:305px;background:var(--soft);text-align:center}
  .services .kicker{margin-top:16px;font-size:9px;font-style:italic;color:var(--muted)}
  .services .sec-title{margin-top:3px}
  .services .desc{margin-top:13px;font-size:6.5px;color:#555}
  .service{width:130px;height:38px;display:flex;text-align:left}
  .service svg{width:38px;height:26px;flex:none;margin-top:6px}
  .service .body{border-left:1px solid var(--blue);padding-left:5px;margin-left:4px}
  .service h3{font-size:5.4px;font-weight:700;color:#333;line-height:1.25;text-transform:uppercase}
  .service p{margin-top:3px;font-size:5.4px;color:#666;line-height:1.25;width:70px}

  /* testimonial */
  .testimonial{left:0;top:747px;width:703px;height:213px;background:linear-gradient(180deg,#2a2523 0%,#3a3330 45%,#4a3a36 75%,#2d2a2c 100%)}
  .testimonial .sec-title{color:var(--white);position:absolute;top:22px;width:703px;text-align:center}
  .underline{width:26px;height:2px;background:var(--blue)}
  .avatar{left:321px;top:62px;width:61px;height:61px;border-radius:50%;border:2px solid var(--white);background:linear-gradient(160deg,#c8a383,#8a6a52)}
  .t-arrow{top:85px;width:24px;height:15px;border:1px solid #aaa;display:flex;align-items:center;justify-content:center}
  .quote-mark{left:134px;top:130px;font-size:42px;font-weight:700;color:var(--blue);font-family:Georgia,serif;line-height:1}
  .testimonial .quote{left:178px;top:138px;width:392px;text-align:center;font-size:7px;line-height:1.6;color:#eee}
  .testimonial .who{left:0;top:185px;width:703px;text-align:center;font-size:7.5px;font-style:italic;color:var(--blue)}

  /* cta */
  .cta{left:0;top:960px;width:703px;height:45px;background:var(--blue)}
  .cta p{left:155px;top:14px;font-size:10px;font-weight:600;font-style:italic;color:var(--white)}
  .cta .btn-free{left:490px;top:12px;width:115px;height:23px;background:#eee;color:#333;font-size:7.5px;display:flex;align-items:center;justify-content:center;gap:10px}

  /* footer */
  .footer{left:0;top:1005px;width:703px;height:163px;background:var(--footer);color:#ccc}
  .f-logo{left:91px;top:15px;width:39px;height:39px;background:var(--white);text-align:center;padding-top:5px}
  .f-logo .mark{width:14px;height:14px;border-radius:50%;border:1.5px solid var(--blue);margin:0 auto 1px}
  .f-logo .name{font-size:5.5px;color:var(--blue)}
  .f-about{left:91px;top:65px;width:142px;font-size:5.6px;line-height:1.55}
  .f-more{left:91px;top:118px;font-size:5.8px;color:var(--blue)}
  .f-social{left:92px;top:141px;display:flex;gap:8px}
  .f-social span{width:12px;height:12px;border-radius:50%;border:1px solid #777;display:block}
  .f-head{top:30px;font-size:7.5px;color:var(--white)}
  .f-links{left:269px;top:70px;font-size:5.8px;line-height:17px}
  .f-contact{left:447px;top:69px;font-size:5.8px}
  .f-contact li{list-style:none;display:flex;align-items:center;gap:8px;height:22px}
  .f-contact svg{width:11px;height:11px}
  .base{left:0;top:1168px;width:703px;height:32px;background:var(--footer-base);font-size:5.6px;color:#888}
  .base .copy{left:91px;top:13px}
  .base .legal{right:94px;top:13px}
</style>
</head>
<body>

<div class="abs topbar">
  <div class="abs socials" aria-label="Social profiles"><span></span><span></span><span></span><span></span><span></span><span></span></div>
  <div class="abs mail">
    <svg width="9" height="6" viewBox="0 0 9 6"><rect width="9" height="6" fill="#0a84c8"/><path d="M0 0l4.5 3.5L9 0" stroke="#fff" stroke-width=".8" fill="none"/></svg>
    Enquiry@brindlelegal-example.com
  </div>
</div>

<header class="abs header">
  <div class="abs logo">
    <div class="mark"></div>
    <div class="name">Brindle Legal</div>
    <div class="tag">Admiralty and Maritime<br>lawyers</div>
  </div>
  <div class="abs share">
    <svg width="14" height="13" viewBox="0 0 14 13"><g stroke="#0a84c8" stroke-width="1.3" fill="none"><circle cx="3" cy="7" r="2"/><circle cx="11" cy="3" r="2"/><circle cx="11" cy="11" r="2"/><path d="M5 6l4-2M5 8l4 2"/></g></svg>
    Share this with your friends
  </div>
  <div class="abs phone">
    <svg class="abs" style="left:1px;top:0" width="13" height="12" viewBox="0 0 13 12"><circle cx="6.5" cy="6" r="5.5" fill="none" stroke="#444" stroke-width="1.4"/><path d="M4 4h5v4H4z" fill="#0a84c8"/></svg>
    <div class="num">0123456789</div>
    <div class="sub">Call Us for Free Consultation</div>
  </div>
  <a class="abs btn-consult">GET FREE CONSULTATION</a>
  <nav class="abs nav">
    <svg width="14" height="11" viewBox="0 0 14 11"><path d="M7 0L0 6h2v5h4V8h2v3h4V6h2z" fill="#0a84c8"/></svg>
    <span style="margin-left:14px">HOME</span><span class="sep">|</span><span>ABOUT</span><span class="sep">|</span><span>LINKS</span><span class="sep">|</span><span>CONTACT</span>
  </nav>
  <div class="abs search">
    <svg width="9" height="9" viewBox="0 0 9 9"><circle cx="3.7" cy="3.7" r="2.8" stroke="#0a84c8" stroke-width="1.3" fill="none"/><path d="M6 6l2.5 2.5" stroke="#0a84c8" stroke-width="1.4"/></svg>
    Search here ...
  </div>
</header>

<section class="abs hero" role="img" aria-label="Photograph of a motor catamaran moored at a marina under a blue sky">
  <h1 class="abs">WE ARE VOICE OF JUSTICE</h1>
  <p class="abs lead">BRINDLE LEGAL IS A BOUTIQUE LAW PRACTICE SPECIALIZING IN ADMIRALTY AND MARITIME LEGAL ADVICE.</p>
  <div class="abs slide-arrow" style="left:6px"><svg width="7" height="11" viewBox="0 0 7 11"><path d="M6 1L1.5 5.5 6 10" stroke="#fff" stroke-width="1.3" fill="none"/></svg></div>
  <div class="abs slide-arrow" style="left:672px"><svg width="7" height="11" viewBox="0 0 7 11"><path d="M1 1l4.5 4.5L1 10" stroke="#fff" stroke-width="1.3" fill="none"/></svg></div>
  <a class="abs btn" style="left:314px;top:196px">READ MORE</a>
</section>

<section class="abs intro">
  <h2 class="sec-title">WE ARE RIGHT <b>FIRM</b></h2>
  <p class="strong">Brindle Legal is a boutique law practice specializing in Admiralty and Maritime legal advice.</p>
  <p class="small">Operating from a base in Queensland, Brindle Legal is able to advise clients in all Australian States and Territories on a wide range of Admiralty and Maritime legal matters</p>
</section>

<section class="abs services">
  <p class="kicker">Our Practice Areas</p>
  <h2 class="sec-title">OUR FEATURED <b>SERVICES</b></h2>
  <p class="desc">We are able to assist by providing cost efficient and effective legal services in relation to:</p>

  <div class="abs service" style="left:93px;top:96px">
    <svg viewBox="0 0 38 26"><path d="M2 15h32l-4 5H7z M10 15l5-5h9l4 5" fill="#0a84c8"/></svg>
    <div class="body"><h3>Domestic Commercial<br>Vessels</h3><p>Lorem Ipsum is simply dummy text of the print-ing and typesetting.</p></div>
  </div>
  <div class="abs service" style="left:221px;top:96px">
    <svg viewBox="0 0 38 26"><circle cx="18" cy="13" r="11" fill="#0a84c8"/><path d="M24 4l10 6-8 2z" fill="#0a84c8"/></svg>
    <div class="body"><h3>International Shipping<br>Vessels</h3><p>Lorem Ipsum is simply dummy text of the print-ing and typesetting.</p></div>
  </div>
  <div class="abs service" style="left:354px;top:96px">
    <svg viewBox="0 0 38 26"><path d="M8 2H4v22h4M30 2h4v22h-4" stroke="#0a84c8" stroke-width="2" fill="none"/><text x="19" y="20" font-size="18" font-family="Open Sans,sans-serif" fill="#0a84c8" text-anchor="middle">$</text></svg>
    <div class="body"><h3>Limitation of Liability<br>Matters</h3><p>Lorem Ipsum is simply dummy text of the print-ing and typesetting.</p></div>
  </div>
  <div class="abs service" style="left:490px;top:96px">
    <svg viewBox="0 0 38 26"><path d="M3 16h32l-5 6H8z M9 16l4-5h12l3 5 M13 11l3-5h6l2 5" fill="none" stroke="#0a84c8" stroke-width="2"/></svg>
    <div class="body"><h3>Superyachts;</h3><p>Lorem Ipsum is simply dummy text of the print-ing and typesetting.</p></div>
  </div>

  <div class="abs service" style="left:93px;top:186px">
    <svg viewBox="0 0 38 26"><path d="M4 10h22M15 10v14M10 24h10M6 4l4 8H4z" stroke="#0a84c8" stroke-width="2" fill="#0a84c8"/><circle cx="28" cy="8" r="5" fill="#0a84c8"/></svg>
    <div class="body"><h3>Australian Coastal<br>Trading</h3><p>Lorem Ipsum is simply dummy text of the print-ing and typesetting.</p></div>
  </div>
  <div class="abs service" style="left:221px;top:186px">
    <svg viewBox="0 0 38 26"><path d="M12 4v20M22 4v20M6 10h24M8 16h22" stroke="#0a84c8" stroke-width="3"/></svg>
    <div class="body"><h3>Offshore Oil and Gas<br>Marine Operations</h3><p>Lorem Ipsum is simply dummy text of the print-ing and typesetting.</p></div>
  </div>
  <div class="abs service" style="left:354px;top:186px">
    <svg viewBox="0 0 38 26"><g stroke="#0a84c8" stroke-width="2" fill="none"><circle cx="19" cy="8" r="5"/><circle cx="12" cy="18" r="5"/><circle cx="26" cy="18" r="5"/><circle cx="19" cy="14" r="2"/></g></svg>
    <div class="body"><h3>Pollution<br>Matters</h3><p>Lorem Ipsum is simply dummy text of the print-ing and typesetting.</p></div>
  </div>
  <div class="abs service" style="left:490px;top:186px">
    <svg viewBox="0 0 38 26"><rect x="3" y="3" width="32" height="20" fill="#0a84c8"/><path d="M9 3v20M15 3v20M21 3v20M27 3v20" stroke="#fff" stroke-width="1"/></svg>
    <div class="body"><h3>Cargo Damage and<br>Disputes</h3><p>Lorem Ipsum is simply dummy text of the print-ing and typesetting.</p></div>
  </div>

  <a class="abs btn" style="left:314px;top:259px">READ MORE</a>
</section>

<section class="abs testimonial" role="img" aria-label="Darkened photograph of stacked steel pipes and cargo on a wharf">
  <h2 class="sec-title">HAPPY <b>CLIENT</b></h2>
  <div class="abs underline" style="left:338px;top:40px"></div>
  <div class="abs t-arrow" style="left:274px"><svg width="10" height="6" viewBox="0 0 10 6"><path d="M10 3H1M3 1L1 3l2 2" stroke="#ccc" fill="none"/></svg></div>
  <div class="abs avatar" role="img" aria-label="Client portrait photo"></div>
  <div class="abs t-arrow" style="left:406px"><svg width="10" height="6" viewBox="0 0 10 6"><path d="M0 3h9M7 1l2 2-2 2" stroke="#ccc" fill="none"/></svg></div>
  <div class="abs quote-mark">&ldquo;</div>
  <p class="abs quote">Lorem Ipsum is simply dummy text of the printing and typesetting.Lorem Ipsum is simply dummy text of the printing and typesetting.Lorem Ipsum is simply dummy text of the printing and typesetting.Lorem Ipsum is simply dummy text of the printing and typesetting.</p>
  <p class="abs who">-Marla Quinn</p>
</section>

<section class="abs cta">
  <p class="abs">If you have any legal problem .....................We are available</p>
  <a class="abs btn-free">FREE CONSULTATION
    <svg width="10" height="8" viewBox="0 0 10 8"><path d="M0 4h9M6 1l3 3-3 3" stroke="#333" stroke-width="1.4" fill="none"/></svg>
  </a>
</section>

<footer class="abs footer">
  <div class="abs f-logo"><div class="mark"></div><div class="name">Brindle Legal</div></div>
  <p class="abs f-about">Lorem Ipsum is simply dummy text of the printing and typesetting industry. Lorem Ipsum has been the industry's standard dummy text ever since the 1500s, when an unknown printer took a galley .</p>
  <a class="abs f-more">Read More &gt;&gt;</a>
  <div class="abs f-social" aria-label="Social profiles"><span></span><span></span><span></span><span></span><span></span><span></span></div>

  <h4 class="abs f-head" style="left:269px">QUICK LINKS</h4>
  <div class="abs f-links"><div>Home</div><div>About</div><div>Links</div><div>Contact</div></div>

  <h4 class="abs f-head" style="left:448px">GET IN TOUCH</h4>
  <ul class="abs f-contact">
    <li><svg viewBox="0 0 11 11"><path d="M5.5 10S2 6.5 2 4a3.5 3.5 0 017 0c0 2.5-3.5 6-3.5 6z" fill="#0a84c8"/><circle cx="5.5" cy="4" r="1.3" fill="#232323"/></svg>Australia</li>
    <li><svg viewBox="0 0 11 11"><path d="M2 1l2 0 1 3-1.5 1a6 6 0 003 3L7.5 6.5l3 1v2C10 10 9 10.5 8 10 4.5 9 2 6.5 1 3 .5 2 1 1 2 1z" fill="#0a84c8"/></svg>0123456789</li>
    <li><svg viewBox="0 0 11 11"><rect y="2" width="11" height="7" fill="#0a84c8"/><path d="M0 2l5.5 4L11 2" stroke="#232323" fill="none"/></svg>Enquiry@brindlelegal-example.com</li>
    <li><svg viewBox="0 0 11 11"><circle cx="5.5" cy="5.5" r="5" fill="#0a84c8"/><path d="M.5 5.5h10M5.5.5c-2 3-2 7 0 10M5.5.5c2 3 2 7 0 10" stroke="#232323" stroke-width=".7" fill="none"/></svg>http://www.brindlelegal-example.com/</li>
  </ul>
</footer>

<div class="abs base">
  <span class="abs copy">Copyright © 2015 Brindle Legal</span>
  <span class="abs legal">Disclaimer &amp; Use Terms &nbsp;| | Privacy Policy</span>
</div>

</body>
</html>
```